Cover Art Needed For Digital Single Release

We are looking to have the cover art designed for a new song called "Paper Lanterns". You will find the track attached below in a private TuneVault link so that you can have a listen.
We are thinking of keeping the artwork fairly simple but still want it to catch your eye. Maybe using the song title and artist’s name in a colorful and creative way. (A well-designed font with a bold color scheme, or even something like a mosaic style art piece featuring the title).
We completely welcome any and all creative visions you might have, even if it strays away from the examples given above.
Thank you in advance for your submissions, and we are excited to collaborate with you!
"Paper Lanterns" by Marcus Holloway
https://tunevault.example/marcusxyz/paper-lanterns/s-r7Tq2wLmNcx
Target Market(s)
Teens/Young Adults
Industry/Entity Type
Music
Requirements
Must have
- An eye-catching design
Should not have
- Please do not rely heavily on stock images. We prefer an original design/concept.

```html
<!DOCTYPE html>
<html lang="en">
<head>
<meta charset="utf-8">
<title>Paper Lanterns — Marcus Holloway</title>
<link href="https://fonts.googleapis.com/css2?family=Anton&family=Kaushan+Script&family=Montserrat:wght@800&display=swap" rel="stylesheet">
<style>
  :root {
    --paper: #e4e4e4;
    --paper-light: #eeeeee;
    --ink-wash: #c4c4c4;
    --ink-wash-deep: #b6b6b6;
    --artist-ink: #111111;
    --script-green: #0b4d44;
    --script-dark: #111614;
    --crimson: #a0062c;
    --crimson-soft: #cf6a80;
  }
  html, body {
    margin: 0;
    padding: 0;
    width: 1200px;
    height: 1200px;
    overflow: hidden;
    background: var(--paper);
  }
  .cover {
    position: relative;
    width: 1200px;
    height: 1200px;
    overflow: hidden;
    background: var(--paper);
  }
  .ink-texture {
    position: absolute;
    inset: 0;
    background:
      radial-gradient(ellipse 420px 560px at 1000px 520px, var(--ink-wash-deep) 0%, rgba(182,182,182,0) 70%),
      radial-gradient(ellipse 520px 420px at 300px 360px, var(--ink-wash) 0%, rgba(196,196,196,0) 70%),
      radial-gradient(ellipse 600px 300px at 600px 1120px, var(--ink-wash) 0%, rgba(196,196,196,0) 70%),
      linear-gradient(160deg, var(--paper-light), var(--paper));
  }
  .artist-name {
    position: absolute;
    top: 72px;
    left: 0;
    width: 1200px;
    margin: 0;
    text-align: center;
    font-family: "Montserrat", sans-serif;
    font-weight: 800;
    font-size: 26px;
    letter-spacing: 0.95em;
    padding-left: 0.95em;
    color: var(--artist-ink);
  }
  .song-title {
    margin: 0;
    font-weight: normal;
  }
  .title-main {
    position: absolute;
    left: 52px;
    top: 760px;
    width: 1100px;
    text-align: center;
    font-family: "Anton", sans-serif;
    font-size: 262px;
    line-height: 1;
    letter-spacing: 2px;
    background: linear-gradient(90deg, var(--crimson-soft) 0%, var(--crimson-soft) 40%, var(--crimson) 62%, var(--crimson) 100%);
    -webkit-background-clip: text;
    background-clip: text;
    color: transparent;
  }
  .title-script {
    position: absolute;
    left: 80px;
    top: 520px;
    width: 800px;
    text-align: center;
    font-family: "Kaushan Script", cursive;
    font-size: 250px;
    line-height: 1.2;
    transform: rotate(-5deg);
    background: linear-gradient(180deg, var(--script-green) 0%, var(--script-green) 40%, var(--script-dark) 100%);
    -webkit-background-clip: text;
    background-clip: text;
    color: transparent;
  }
</style>
</head>
<body>
  <main class="cover">
    <div class="ink-texture" role="img" aria-label="Grey ink splatter and wash texture on light paper"></div>
    <p class="artist-name">MARCUS HOLLOWAY</p>
    <h1 class="song-title">
      <span class="title-main">LANTERNS</span>
      <span class="title-script">Paper</span>
    </h1>
  </main>
</body>
</html>
```